Flashy and colorful banner for an orange grower

Hi, I need a graphic for an advertising banner (80x200cm) to be placed next to the sales van. So far we have tried to highlight the naturalness of our products. With this banner we would like to highlight the ancient Sicilian tradition, with the typical decorations, I attach some photos as an example. We will sell our products far from Sicily, so I would like to exalt our origin.
We would like to dare with a colorful and amazing design, to capture the attention of passers-by.
It might be nice to insert or rework the decoration within our logo.
I would like to insert 4 of our offers inside the banner, only in the upper part, from the middle up.
The text is:
DAL CUORE DELLA SICILIA
ARANCIA TAROCCO
ALLA RINFUSA
5€ BORSA
DA SPREMERE
10€ CASSETTA
DA TAVOLA
15€ CASSETTA
SELEZIONE PREMIUM
20€ CASSETTA
Thanks for your time

```html
<!DOCTYPE html>
<html lang="it">
<head>
<meta charset="utf-8">
<title>Dal cuore della Sicilia – Arancia Tarocco</title>
<link rel="stylesheet" href="https://fonts.googleapis.com/css2?family=Fredoka:wght@600;700&family=Limelight&family=Anton&family=Montserrat:wght@600&display=swap">
<style>
  :root {
    --cream: #eee6d4;
    --cream-light: #f4eedf;
    --green: #1d6a2b;
    --green-dark: #134f1e;
    --title-green: #1c6a33;
    --orange: #f3892a;
    --orange-deep: #e35a25;
    --price-disc: #ec7b45;
    --white: #ffffff;
  }
  html, body {
    margin: 0;
    padding: 0;
    width: 1200px;
    height: 2400px;
    overflow: hidden;
    background: var(--cream);
  }
  .banner {
    display: block;
    width: 1200px;
    height: 2400px;
  }
  .offer-title {
    font-family: "Fredoka", sans-serif;
    font-weight: 700;
    fill: var(--title-green);
    font-size: 46px;
  }
  .offer-price {
    font-family: "Anton", sans-serif;
    fill: var(--white);
    font-size: 84px;
  }
  .offer-unit {
    font-family: "Anton", sans-serif;
    fill: var(--white);
    font-size: 34px;
  }
  .headline-small {
    font-family: "Fredoka", sans-serif;
    font-weight: 700;
    fill: var(--white);
    font-size: 112px;
  }
  .headline-della {
    font-family: "Limelight", sans-serif;
    fill: var(--white);
    font-size: 200px;
  }
  .headline-sicilia {
    font-family: "Limelight", sans-serif;
    fill: var(--orange);
    font-size: 200px;
  }
  .product-name {
    font-family: "Montserrat", sans-serif;
    font-weight: 600;
    fill: var(--white);
    font-size: 44px;
  }
  .brand-name {
    font-family: "Fredoka", sans-serif;
    font-weight: 600;
    fill: var(--title-green);
    font-size: 76px;
  }
</style>
</head>
<body>
<svg class="banner" viewBox="0 0 1200 2400" xmlns="http://www.w3.org/2000/svg">
  <defs>
    <radialGradient id="patternTone" cx="50%" cy="45%" r="75%">
      <stop offset="0" stop-color="#f5efe0"/>
      <stop offset="0.55" stop-color="#f3e6c6"/>
      <stop offset="1" stop-color="#f0d9ad"/>
    </radialGradient>
    <radialGradient id="ringTone" cx="50%" cy="50%" r="50%">
      <stop offset="0.82" stop-color="#f3e3c4"/>
      <stop offset="0.85" stop-color="#2f7a35"/>
      <stop offset="0.89" stop-color="#f6a24a"/>
      <stop offset="0.95" stop-color="#f08a2e"/>
      <stop offset="0.97" stop-color="#2f7a35"/>
      <stop offset="1" stop-color="#ee7f2c"/>
    </radialGradient>
    <radialGradient id="sliceTone" cx="50%" cy="55%" r="52%">
      <stop offset="0" stop-color="#f59a3c"/>
      <stop offset="0.7" stop-color="#f07e26"/>
      <stop offset="0.82" stop-color="#2f7a35"/>
      <stop offset="0.88" stop-color="#f3e3c4"/>
      <stop offset="1" stop-color="#ef8a2e"/>
    </radialGradient>
    <radialGradient id="greenTone" cx="50%" cy="50%" r="65%">
      <stop offset="0" stop-color="#217330"/>
      <stop offset="1" stop-color="#135020"/>
    </radialGradient>
    <radialGradient id="splashTone" cx="50%" cy="50%" r="50%">
      <stop offset="0" stop-color="#f39a2a"/>
      <stop offset="0.6" stop-color="#f5b443" stop-opacity="0.85"/>
      <stop offset="1" stop-color="#f3b24a" stop-opacity="0"/>
    </radialGradient>
    <radialGradient id="logoTone" cx="50%" cy="50%" r="50%">
      <stop offset="0" stop-color="#f39a35"/>
      <stop offset="0.85" stop-color="#f07e26"/>
      <stop offset="1" stop-color="#e8c48a"/>
    </radialGradient>
  </defs>

  <!-- upper backdrop -->
  <rect class="backdrop-pattern" x="0" y="0" width="1200" height="1200" fill="url(#patternTone)" role="img" aria-label="Decorazione siciliana di maioliche in toni crema e arancio chiaro"/>

  <!-- offers -->
  <g class="offer">
    <circle cx="340" cy="210" r="200" fill="url(#ringTone)" role="img" aria-label="Cornice decorata in stile carretto siciliano"/>
    <text class="offer-title" x="340" y="116" text-anchor="middle">ALLA</text>
    <text class="offer-title" x="340" y="158" text-anchor="middle" textLength="215" lengthAdjust="spacingAndGlyphs">RINFUSA</text>
    <circle cx="340" cy="272" r="100" fill="var(--price-disc)"/>
    <text class="offer-price" x="340" y="290" text-anchor="middle">5€</text>
    <text class="offer-unit" x="340" y="330" text-anchor="middle">BORSA</text>
  </g>
  <g class="offer">
    <circle cx="860" cy="210" r="200" fill="url(#ringTone)" role="img" aria-label="Cornice decorata in stile carretto siciliano"/>
    <text class="offer-title" x="855" y="116" text-anchor="middle">DA</text>
    <text class="offer-title" x="855" y="158" text-anchor="middle" textLength="240" lengthAdjust="spacingAndGlyphs">SPREMERE</text>
    <circle cx="855" cy="272" r="100" fill="var(--price-disc)"/>
    <text class="offer-price" x="855" y="290" text-anchor="middle">10€</text>
    <text class="offer-unit" x="855" y="330" text-anchor="middle" textLength="160" lengthAdjust="spacingAndGlyphs">CASSETTA</text>
  </g>
  <g class="offer">
    <circle cx="340" cy="655" r="200" fill="url(#ringTone)" role="img" aria-label="Cornice decorata in stile carretto siciliano"/>
    <text class="offer-title" x="340" y="563" text-anchor="middle">DA</text>
    <text class="offer-title" x="340" y="605" text-anchor="middle" textLength="190" lengthAdjust="spacingAndGlyphs">TAVOLA</text>
    <circle cx="340" cy="716" r="100" fill="var(--price-disc)"/>
    <text class="offer-price" x="340" y="734" text-anchor="middle">15€</text>
    <text class="offer-unit" x="340" y="774" text-anchor="middle" textLength="160" lengthAdjust="spacingAndGlyphs">CASSETTA</text>
  </g>
  <g class="offer">
    <circle cx="860" cy="660" r="200" fill="url(#ringTone)" role="img" aria-label="Cornice decorata in stile carretto siciliano"/>
    <text class="offer-title" x="858" y="568" text-anchor="middle" textLength="228" lengthAdjust="spacingAndGlyphs">SELEZIONE</text>
    <text class="offer-title" x="858" y="610" text-anchor="middle" textLength="200" lengthAdjust="spacingAndGlyphs">PREMIUM</text>
    <circle cx="860" cy="720" r="100" fill="var(--price-disc)"/>
    <text class="offer-price" x="860" y="738" text-anchor="middle">20€</text>
    <text class="offer-unit" x="860" y="778" text-anchor="middle" textLength="160" lengthAdjust="spacingAndGlyphs">CASSETTA</text>
  </g>

  <!-- central orange slice -->
  <circle class="orange-slice" cx="600" cy="1210" r="345" fill="url(#sliceTone)" role="img" aria-label="Fetta d'arancia con decorazioni siciliane"/>

  <!-- green band -->
  <path class="accent-band" d="M0,940 Q600,1320 1200,940 L1200,2100 L0,2100 Z" fill="var(--orange-deep)"/>
  <path class="green-band" d="M0,990 Q600,1400 1200,990 L1200,2100 L0,2100 Z" fill="url(#greenTone)" role="img" aria-label="Sfondo verde con arance in trasparenza"/>

  <!-- headline -->
  <text class="headline-small" x="600" y="1335" text-anchor="middle" textLength="560" lengthAdjust="spacingAndGlyphs">DAL CUORE</text>
  <text class="headline-della" x="600" y="1507" text-anchor="middle" textLength="925" lengthAdjust="spacingAndGlyphs">DELLA</text>
  <text class="headline-sicilia" x="610" y="1682" text-anchor="middle" textLength="955" lengthAdjust="spacingAndGlyphs">SICILIA</text>
  <text class="product-name" x="600" y="1752" text-anchor="middle" textLength="945" lengthAdjust="spacing">ARANCIA TAROCCO</text>

  <!-- footer -->
  <path class="accent-band" d="M0,2040 Q600,1540 1200,2040 L1200,2400 L0,2400 Z" fill="var(--orange-deep)"/>
  <path class="footer" d="M0,2080 Q600,1600 1200,2080 L1200,2400 L0,2400 Z" fill="var(--cream)"/>
  <ellipse cx="150" cy="2140" rx="190" ry="170" fill="url(#splashTone)" role="img" aria-label="Spruzzi di succo d'arancia con spicchi"/>
  <ellipse cx="1060" cy="2120" rx="190" ry="180" fill="url(#splashTone)" role="img" aria-label="Spruzzi di succo d'arancia con arance"/>

  <g class="brand">
    <circle cx="608" cy="2078" r="108" fill="url(#logoTone)"/>
    <text class="brand-name" x="605" y="2232" text-anchor="middle" textLength="560" lengthAdjust="spacing">SOLEVERDE</text>
  </g>
</svg>
</body>
</html>
```